Honey Label Design (145 × 55 mm) – Premium / Minimal Style

Project Description
I am looking for a professional label design for a 500 g honey jar (twist-off, copper-colored lid).
The design should look premium, elegant, and minimal, reflecting natural quality and regional authenticity.
I expect two design proposals from each designer:

One concept based strictly on my color and style guidelines
One completely free creative concept (designer's own interpretation)

⚠️ Important: The layout and positioning of all elements must follow my specifications exactly (see below). Creativity is welcome in style, colors, and typography—but not in layout structure and content.

Label Size and Constraints

Final size: 145 mm × 55 mm (landscape)
All elements must remain fully within the label area
No part (especially the hexagon) may extend beyond the label boundaries

Design Style

Minimal, clean, premium
No clutter, no excessive colors
Preferred colors:

Warm natural tones (honey, beige, brown)
Inspired by the branding of: www.wabenhof-laden. de
Subtle copper tone accents (to match the lid)

Background

Very subtle illustrated/sketched background
Motif:

Wildflower meadow (foreground)
Mixed forest (background)

Style should be fine line / sketch style, not photorealistic
The background must remain very soft so text remains clearly readable

Central Element (Mandatory)

A hexagon (honeycomb shape) centered on the label
Inside text:

“GERMAN HONEY”
“500 g”

The hexagon must be:

Fully inside the label (no overlapping, my example is wrong)
Visually balanced and centered

Left Text Block (Important)
The following content (in german) must be placed left-aligned (not centered!):
Bottling point:
Henrik Dollmann Beekeeping
Lindenkamper Weg 17
07318 Saalfeld
Tel.: 03671 5274061
mail@wabenhof-laden.example
Typography must be clean and clearly structured.

Mandatory White Fields (Very Important)
There must be exactly 3 white boxes:
Size:

Each: 28 mm × 12 mm
No visible border

Positioning (must follow exactly):

Bottom center

Completely blank (for honey type)

Right side – upper field

Text above: “Best before:”

Right side – lower field (directly below)

Text above: “Lot number”

⚠️ All three fields must:

Be identical in size
Be perfectly aligned
Match the layout shown in the reference image

Layout Rules (Strict)

The arrangement of elements is fixed and must not be changed
Center field must be directly below the hexagon
Right-side fields must be vertically aligned
Left text must remain left-aligned

goal
The label should communicate:

High quality / premium honey
Regional trust and authenticity
Clean and professional print-ready design

Reference
A reference image is provided showing:

exact placement of all fields
general layout structure

⚠️ The reference is for layout guidance only — not for copying design style.
Updates

All mandatory information must be in German like the address
Bottling point:
Henrik Dollmann Beekeeping
Lindenkamper W. 17
07318 Saalfeld
Tel.: 03671 5274061
www.wabenhof-laden.example

Target Market(s)

Germany

Font styles to use
Sans Serif
Other font styles liked:
• Montserrat, Open Sans, Libre Baskerville

Colors
00AB8E
00BBA5
67D7C9
C6EFE9
E9F9F6
59FF00
82FF00
B8FF75
E3FFCB
F4FFEA
FFF300
FFF600
FEFA6F
FFFEC7
FFFEE8
FFC000
F8CF3A
FAE287
FDF2CF
FEFAEE
F0912C
F2A743
F7CA91
FBE8D2
FDF5EE
EE7325
F08F49
F5BC92
FAE3D3
FDF4ED

Requirements
Must have
• Mandatory Information on Honey Labels (Germany / EU) (Product Name, Country of origin, Net quantity, Minimum durability date (placeholder), Name and address of the food business operator, Batch / lot identification (placeholder), Special warning for infants “Not suitable for infants under 12 months”

```html
<!DOCTYPE html>
<html lang="de">
<head>
<meta charset="utf-8">
<title>Deutscher Honig – Etikett 500 g</title>
<link rel="stylesheet" href="https://fonts.googleapis.com/css2?family=Libre+Baskerville:wght@700&family=Nunito+Sans:wght@400;800&display=swap">
<style>
  :root {
    --paper: #f8ecd2;
    --paper-light: #fbf3e2;
    --paper-deep: #eedcb6;
    --copper: #c4801e;
    --copper-dark: #a8651a;
    --ink: #3b2612;
    --text: #2e2418;
    --field: #fdfdfb;
  }
  * { margin: 0; padding: 0; box-sizing: border-box; }
  html, body { width: 1200px; height: 456px; overflow: hidden; background: var(--paper); }
  .label {
    position: relative;
    width: 1200px; height: 456px;
    background: var(--paper);
    font-family: "Nunito Sans", sans-serif;
    color: var(--text);
  }
  .backdrop {
    position: absolute; inset: 8px;
    border-radius: 10px;
    background:
      linear-gradient(180deg, var(--paper-light) 0%, var(--paper-deep) 22%, var(--paper) 42%, var(--paper) 62%, var(--paper-deep) 100%);
  }
  .frame { position: absolute; inset: 0; }
  .producer {
    position: absolute; left: 114px; top: 164px;
    line-height: 1;
  }
  .producer p { position: absolute; left: 0; white-space: nowrap; font-size: 16px; }
  .producer .intro { top: 2px; }
  .producer .name { top: 27px; font-size: 19px; font-weight: 800; color: var(--ink); }
  .producer .street { top: 60px; }
  .producer .city { top: 88px; }
  .producer .phone { top: 115px; }
  .producer .web { top: 141px; font-size: 15px; }
  .product-mark {
    position: absolute; left: 549px; top: 56px; width: 102px; height: 80px;
    border-radius: 14px;
    background: radial-gradient(circle at 55% 50%, #f3a437 0%, #e8962c 45%, rgba(248,236,210,0) 75%);
    opacity: 0.85;
  }
  .product-name {
    position: absolute; left: 405px; width: 390px; text-align: center;
    font-family: "Libre Baskerville", serif; font-weight: 700; color: var(--ink);
    line-height: 1; white-space: nowrap;
  }
  .product-name.line-one { top: 148px; font-size: 40px; letter-spacing: 3px; }
  .product-name.line-two { top: 190px; font-size: 66px; letter-spacing: 5px; }
  .net-quantity {
    position: absolute; left: 405px; width: 390px; top: 286px; text-align: center;
    font-family: "Libre Baskerville", serif; font-weight: 700; font-size: 36px;
    color: var(--copper); line-height: 1;
  }
  .info-fields { position: absolute; left: 860px; top: 0; }
  .info-fields .field-label {
    position: absolute; left: 5px; white-space: nowrap; font-size: 16px; line-height: 1;
  }
  .field {
    position: absolute; left: 0; width: 213px; height: 44px; background: var(--field);
  }
  .variety-field { left: 493px; top: 392px; }
  .warning {
    position: absolute; left: 865px; top: 300px; font-size: 10.5px; white-space: nowrap; line-height: 1;
  }
</style>
</head>
<body>
<main class="label">
  <div class="backdrop" role="img" aria-label="Feine Skizze im Hintergrund: Wildblumenwiese im Vordergrund und Mischwald mit Hügeln dahinter, in warmen Beige- und Honigtönen"></div>

  <svg class="frame" width="1200" height="456" viewBox="0 0 1200 456" aria-hidden="true">
    <rect x="8.5" y="8.5" width="1183" height="439" rx="10" fill="none" stroke="var(--copper)" stroke-width="2"/>
    <rect x="14.5" y="14.5" width="1171" height="427" rx="8" fill="none" stroke="var(--copper)" stroke-width="0.8" opacity="0.7"/>
    <polygon points="600,19 795,110 795,290 600,378 405,290 405,110" fill="var(--paper-light)" stroke="var(--copper)" stroke-width="5" stroke-linejoin="round"/>
    <polygon points="600,32 783,117 783,283 600,365 417,283 417,117" fill="none" stroke="var(--copper)" stroke-width="1.2"/>
    <line x1="507" y1="270" x2="590" y2="270" stroke="var(--copper)" stroke-width="1.6"/>
    <line x1="610" y1="270" x2="693" y2="270" stroke="var(--copper)" stroke-width="1.6"/>
    <circle cx="600" cy="270" r="4.5" fill="var(--copper-dark)"/>
  </svg>

  <section class="producer">
    <p class="intro">Abgefüllt von:</p>
    <p class="name">Imkerei Henrik Dollmann</p>
    <p class="street">Lindenkamper W. 17</p>
    <p class="city">07318 Saalfeld</p>
    <p class="phone">Tel.: 03671 5274061</p>
    <p class="web">www.wabenhof-laden.example</p>
  </section>

  <div class="product-mark" role="img" aria-label="Bildmarke: Biene auf Honigwaben in Orange und Dunkelgrau"></div>
  <h1>
    <span class="product-name line-one">DEUTSCHER</span>
    <span class="product-name line-two">HONIG</span>
  </h1>
  <div class="net-quantity">500 g</div>

  <div class="field variety-field" aria-label="Feld für die Sorte"></div>

  <section class="info-fields">
    <span class="field-label" style="top:136px">Mindestens haltbar bis</span>
    <div class="field" style="top:158px"></div>
    <span class="field-label" style="top:218px">Losnummer</span>
    <div class="field" style="top:239px"></div>
  </section>

  <p class="warning">Nicht geeignet für Säuglinge unter 12 Monaten.</p>
</main>
</body>
</html>
```